Side of Page Partnership-type Letterhead Design for Chiropractic Office

Side oriented letterhead with practice locations/demographics, physician names and company logo

Target Market(s)

Healthcare Professionals & Attorneys

Industry/Entity Type

Healthcare

Font styles to use
Other font styles liked:
• Font of Logo is Trajan Pro, but not a deal breaker if we try something else

Colors

Designer to choose colors to be used in the design.

Requirements
Must have
• All info from attached documents

```html
<!DOCTYPE html>
<html lang="en">
<head>
<meta charset="utf-8">
<title>Keystone Chiropractic Letterhead</title>
<link href="https://fonts.googleapis.com/css2?family=Carlito:wght@400;700&family=Lato:wght@700&display=swap" rel="stylesheet">
<style>
:root{
  --backdrop:#e6e6e6;
  --paper:#ffffff;
  --ink:#1a1a1a;
  --ink-soft:#333333;
  --brand:#3b3b3b;
  --rule-blue:#5b7fc4;
  --rule-orange:#f0a83c;
  --accent-green:#6aa84f;
  --signature-tone:#e9e9e9;
}
*{margin:0;padding:0;box-sizing:border-box}
html,body{width:1066px;height:1200px;overflow:hidden;background:var(--backdrop)}
.letterhead{position:absolute;left:69px;top:0;width:928px;height:1200px;background:var(--paper);color:var(--ink);font-family:"Carlito",Calibri,sans-serif}
.brand-name{position:absolute;left:560px;top:86px;width:300px;text-align:right;font-family:"Carlito",Calibri,sans-serif;font-weight:400;color:var(--brand);font-size:31px;line-height:30px;letter-spacing:1px;text-transform:uppercase}
.brand-name span{display:block;font-size:24px;letter-spacing:.5px}
.brand-dot{position:absolute;left:868px;top:96px;width:28px;height:28px;border-radius:50%;background:var(--accent-green)}
.sidebar{position:absolute;left:59px;top:0;font-family:"Lato",Arial,sans-serif;font-weight:700;color:var(--ink);font-size:12.5px}
.doctor-list{position:absolute;top:197px;list-style:none;white-space:nowrap}
.doctor-list li{height:30.4px}
.location{position:absolute;white-space:nowrap;letter-spacing:-.2px}
.location h3{font-size:12.5px;font-weight:700;height:26px}
.location address{font-style:normal;font-weight:400;font-size:12.5px;line-height:15.5px;height:41px}
.location p{height:25.5px}
.loc-northfield{top:456px}
.loc-brookhaven{top:626px}
.loc-millbrook{top:796px}
.sidebar-mark{position:absolute;left:95px;top:1005px;width:70px;height:70px;border-radius:50%;background:var(--accent-green)}
.divider{position:absolute;left:238px;top:198px;width:6px;height:1002px}
.content{position:absolute;left:282px;top:0;width:570px;font-size:15.5px;color:var(--ink-soft)}
.recipient{position:absolute;top:198px;font-weight:700;color:var(--ink);line-height:32px;white-space:nowrap}
.body-copy{position:absolute;width:570px;line-height:31.8px;letter-spacing:.05px}
.para-1{top:356px}
.para-2{top:547px}
.para-3{top:769px}
.closing{position:absolute;top:961px;line-height:31.8px}
.signature{position:absolute;left:0;top:990px;width:194px;height:86px;background:var(--signature-tone);border-radius:4px}
.sign-title{position:absolute;top:1088px;line-height:31.8px;white-space:nowrap}
</style>
</head>
<body>
<main class="letterhead">
  <header>
    <div class="brand-name">Keystone<span>Chiropractic</span></div>
    <div class="brand-dot"></div>
  </header>

  <aside class="sidebar">
    <ul class="doctor-list">
      <li>Daniel Whitcombe, DC, DACNB</li>
      <li>Martin Whitcombe, DC</li>
      <li>Grant Ellery, DC</li>
      <li>Travis Holloway, DC</li>
      <li>Owen Prescott, DC</li>
      <li>Lucas Brennard, DC</li>
      <li>Evan Calder, DC</li>
    </ul>
    <section class="location loc-northfield">
      <h3>Northfield</h3>
      <address>4120 N. Meadow Ave.<br>Northfield, OH 43990</address>
      <p>P: 555-210-4400</p>
      <p>F: 555-210-4401</p>
    </section>
    <section class="location loc-brookhaven">
      <h3>Brookhaven</h3>
      <address>517 Elm Park Rd.<br>Brookhaven, OH 43991</address>
      <p>P: 555-318-2200</p>
      <p>F: 555-318-2201</p>
    </section>
    <section class="location loc-millbrook">
      <h3>Millbrook</h3>
      <address>286 S. Linden Rd<br>Millbrook, OH 43992</address>
      <p>P: 555-472-6600</p>
      <p>F: 555-472-6601</p>
    </section>
  </aside>
  <div class="sidebar-mark"></div>

  <svg class="divider" viewBox="0 0 6 1002" preserveAspectRatio="none" aria-hidden="true">
    <line x1="1" y1="0" x2="1" y2="1002" stroke="var(--rule-orange)" stroke-width="1.2"/>
    <line x1="3" y1="0" x2="3" y2="1002" stroke="var(--rule-blue)" stroke-width="1.2"/>
    <line x1="5" y1="0" x2="5" y2="1002" stroke="var(--rule-orange)" stroke-width="1.2"/>
  </svg>

  <section class="content">
    <div class="recipient">
      To<br>
      Lorem Ipsum is simply<br>
      Lorem Ipsum is Lorem Ipsum is<br>
      Lorem Ipsum is
    </div>
    <p class="body-copy para-1">&nbsp;dummy text of the printing and typesetting industry. Lorem Ipsum has been the industry's standard dummy text ever since the 1500s, when an unknown printer took a galley of type and scrambled it to make a type specimen book. It has survived not only five centuries, but also the leap into electronic type&shy;setting, remaining essentially unchanged.</p>
    <p class="body-copy para-2">It is a long established fact that a reader will be distracted by the readable content of a page when looking at its layout. The point of using Lorem Ipsum is that it has a more-or-less normal distribution of letters, as opposed to using 'Content here, content here', making it look like readable English. Many desktop publishing packages and web page editors now use Lorem Ipsum as their default model text, and a search for 'lorem .</p>
    <p class="body-copy para-3">&nbsp;Contrary to popular belief, Lorem Ipsum is not simply random text. It has roots in a piece of classical Latin literature from 45 BC, making it over 2000 years old. Edwin Larrow, a Latin professor at Fairmont Ridge College in Virginia, looked up one of the more obscure Latin words, consectetur, from a Lorem Ipsum passage,</p>
    <p class="closing">Lorem Ipsum</p>
    <div class="signature" role="img" aria-label="Handwritten signature"></div>
    <p class="sign-title">Lorem Ipsum is a dummy</p>
  </section>
</main>
</body>
</html>
```